URGENT website build for kids rugby company

We have created a new company that has venues all over London coaching kids age 2-7 fun rugby based activities. This is an urgent job that needs to be finished within 3 weeks.

We need a website built within the next 2-3 weeks that shows all our venues and details of each with a dedicated page that would have a location map, times or lessons, coach profiles and a "book here" button. The site must enable clients to book their "free trial" or "term membership" on the website. This will mean working with our payment company call Coinbridge Pay, and a CRM booking management site (to be confirmed on Monday 25th Nov). We must have the ability to create a new venue page at any time.

The front page would have a slide show of editable pictures, an intro text area under the picture frame. It would need to have a number of promo boxes on it as well.

It would have a few other pages of info such as:
A page explaining in detail our age groups of which there are 3 (red, green and blue)
how the lessons work and activity examples
terms and conditions
kit you can buy

I will give a more detailed brief on conversation with applicants for the job

It needs to be a kid AND mum friendly design. with easy and familiar usability and as uncluttered as possible. Corporate colours are red, black and white.

• These are website designs I like and would aspire to have a similar feel to:
• http://www.morvale-studio.com/
• http://www.quillandroe.com/
• http://www.tobrask.com
• Site similar to our company include the following - but we do NOT want to look like these but the site content is relevant:
• http://www.pennyhoppers.co.uk/
• http://www.scrumotts.com/
• http://www.zestodmunchway.com/site/

```html
<!DOCTYPE html>
<html lang="en">
<head>
<meta charset="utf-8">
<title>Tryline Tots – Fun Rugby Activities</title>
<link href="https://fonts.googleapis.com/css2?family=Lato:ital,wght@0,300;0,400;0,700;1,400&family=Open+Sans:ital,wght@0,400;0,600;1,400&display=swap" rel="stylesheet">
<style>
:root{
  --red:#b5121b;
  --red-bright:#d42a2a;
  --ink:#333;
  --text:#555;
  --muted:#777;
  --line:#dcdcdc;
  --panel:#f3f3f3;
  --grass:#4d6a28;
  --footer:#3a3a3a;
  --footer-base:#2c2c2c;
  --footer-text:#c8c8c8;
  --white:#fff;
}
*{box-sizing:border-box;margin:0;padding:0}
html,body{width:833px;height:1200px;overflow:hidden;background:var(--white)}
body{position:relative;font-family:'Open Sans',Arial,sans-serif;color:var(--text)}
.abs{position:absolute}

/* header */
.brand{left:128px;top:12px;display:flex;align-items:center;gap:8px}
.brand-dot{width:40px;height:40px;border-radius:50%;background:var(--red)}
.brand-name{font-family:'Lato',sans-serif;font-weight:700;font-size:19px;line-height:19px;color:var(--red);text-transform:uppercase;width:90px}
.call{right:127px;top:10px;font-family:'Lato',sans-serif;font-size:11px;color:var(--red)}
.social{right:127px;top:33px;display:flex;gap:10px}
.social span{width:12px;height:12px;border-radius:50%;background:var(--ink)}

/* nav */
.nav{left:0;top:60px;width:833px;height:41px;border-top:1px solid #eee;border-bottom:1px solid #eee;background:linear-gradient(#fff,#f7f7f7)}
.nav ul{list-style:none;position:absolute;left:376px;top:-1px;display:flex;height:41px}
.nav li{height:41px;line-height:41px;font-size:9px;text-transform:uppercase;color:var(--ink);border-left:1px solid #e2e2e2;text-align:center}
.nav li:last-child{border-right:1px solid #e2e2e2}
.nav li.active{background:var(--red);color:var(--white);border-color:var(--red)}

/* hero */
.hero{left:0;top:100px;width:833px;height:257px;background:var(--grass)}
.hero-photo{left:127px;top:0;width:579px;height:257px;background:linear-gradient(180deg,#7a8a5a 0%,#6d8840 45%,#557a2a 100%)}
.hero-caption{left:144px;top:134px;width:300px;font-family:'Lato',sans-serif;font-size:11.5px;line-height:16px;color:var(--white)}
.btn-read{left:141px;top:197px;width:68px;height:25px;background:var(--red-bright);color:var(--white);font-family:'Lato',sans-serif;font-size:9.5px;line-height:25px;text-align:center;border-radius:2px;text-transform:uppercase}
.hero-dots{left:393px;top:223px;display:flex;gap:6px}
.hero-dots span{width:8px;height:8px;border-radius:50%;background:rgba(255,255,255,.5)}
.arrow{top:102px}

/* intro */
.intro-title{left:0;top:374px;width:833px;text-align:center;font-family:'Lato',sans-serif;font-weight:300;font-size:24px;color:var(--red)}
.intro-text{left:136px;top:413px;width:561px;text-align:center;font-family:'Lato',sans-serif;font-size:10.5px;line-height:14px;color:var(--text)}

/* promo boxes */
.promo{top:527px;width:185px;height:155px;background:var(--panel);border:1px solid var(--line);text-align:center}
.promo h3{margin-top:22px;font-family:'Lato',sans-serif;font-weight:400;font-size:17px;color:var(--red)}
.promo p{margin:10px auto 0;width:156px;font-size:7.4px;line-height:11px;color:var(--text)}
.more{display:inline-block;margin-top:10px;height:11px;line-height:11px;padding:0 4px 0 6px;background:#ddd;font-size:6.8px;color:var(--muted)}
.more b{font-weight:400;margin-left:8px}
.promo-icon{top:475px;width:66px;height:66px;border-radius:50%;background:var(--ink);border:2px solid #fff;box-shadow:0 0 0 1px var(--line)}
.promo-icon svg{position:absolute;left:17px;top:17px}

/* how it works */
.section-title{top:722px;font-family:'Lato',sans-serif;font-weight:300;font-size:17px;color:var(--red)}
.rule{left:127px;top:753px;width:382px;height:1px;background:var(--line)}
.tabs{left:127px;top:778px;width:136px;list-style:none;border-top:1px solid #e8e8e8}
.tabs li{height:30px;line-height:30px;padding-left:13px;font-size:7.6px;color:var(--ink);border:1px solid #e8e8e8;border-top:0}
.tabs li.active{color:var(--red);font-weight:600}
.groups{left:291px;top:786px;width:220px}
.group{display:flex;gap:10px;margin-bottom:13px}
.group p{font-size:7.6px;line-height:11.5px;color:var(--text)}
.group strong{font-weight:400;color:var(--ink)}

/* testimonial */
.quote{left:521px;top:753px;width:186px;height:151px;background:#f5f5f5;padding:18px 14px}
.quote p{font-style:italic;font-size:7.6px;line-height:11.5px;color:var(--ink)}
.quote cite{position:absolute;right:13px;top:123px;font-style:italic;font-size:9px;color:var(--red)}

/* footer */
.footer-shade{left:0;top:948px;width:833px;height:8px;background:#e6e6e6}
.footer{left:0;top:956px;width:833px;height:210px;background:var(--footer)}
.footer-base{left:0;top:1165px;width:833px;height:35px;background:var(--footer-base)}
.copyright{right:126px;top:1177px;font-size:7.6px;color:var(--footer-text)}
.fcol{top:993px;width:138px;font-size:7.6px;line-height:11px;color:var(--footer-text)}
.fcol h4{font-family:'Lato',sans-serif;font-weight:400;font-size:9.5px;color:var(--white);text-transform:uppercase;margin-bottom:14px}
.fcol .date{color:var(--red-bright);margin-bottom:4px}
.fcol .post{margin-bottom:12px}
.contact-line{display:flex;gap:8px;align-items:flex-start;margin-top:12px}
.contact-line svg{flex:none;margin-top:1px}
.subscribe{display:flex;gap:2px;margin-top:13px}
.subscribe .field{width:90px;height:17px;background:#2e2e2e;border:1px solid #4a4a4a;font-size:6.5px;line-height:15px;padding-left:6px;color:#999}
.subscribe .send{width:45px;height:17px;background:#2e2e2e;border:1px solid #555;font-size:7px;line-height:15px;text-align:center;color:#bbb;text-transform:uppercase}
</style>
</head>
<body>

<header>
  <div class="brand abs"><span class="brand-dot"></span><span class="brand-name">Tryline Tots</span></div>
  <div class="call abs">Call : +00 44 908172</div>
  <div class="social abs" aria-label="Social links"><span></span><span></span><span></span><span></span><span></span></div>
</header>

<nav class="nav abs">
  <ul>
    <li class="active" style="width:68px">Home</li>
    <li style="width:68px">About Us</li>
    <li style="width:68px">Venue</li>
    <li style="width:67px">Rugby Kit</li>
    <li style="width:68px">Contact Us</li>
  </ul>
</nav>

<section class="hero abs">
  <div class="hero-photo abs" role="img" aria-label="Photo of children in rugby shirts running across a grass pitch with a ball"></div>
  <svg class="arrow abs" style="left:37px" width="24" height="44" viewBox="0 0 24 44"><path d="M22 1 2 22l20 21" fill="none" stroke="#fff" stroke-width="2"/></svg>
  <svg class="arrow abs" style="left:778px" width="24" height="44" viewBox="0 0 24 44"><path d="M2 1l20 21L2 43" fill="none" stroke="#fff" stroke-width="2"/></svg>
  <p class="hero-caption abs">Lorem ipsum dolor sit amet, consectetuer adipiscing elit, sed diam nonummy nibh euismod tincidunt ut laoreet dolore magna aliquam erat volutpat.</p>
  <div class="btn-read abs">Read More</div>
  <div class="hero-dots abs"><span></span><span></span><span></span></div>
</section>

<h1 class="intro-title abs">Welcome to Fun Rugby Activities</h1>
<p class="intro-text abs">Lorem Ipsum has been the industry's standard dummy text ever since the 1500s, when an unknown printer took a galley of type and scrambled it to make a type specimen book.This is the an intro text area under the picture frame.</p>

<article class="promo abs" style="left:127px">
  <h3>Locations</h3>
  <p>Lorem ipsum dolor sit amet, consectetur adipisicing elit, sed do eiusmod tempor incididunt ut labore et dolore magna aliqua. Ut enim ad minim veniam, quis nostrud exercitation ullamco laboris nisi ut aliquip ex ea commodo consequat.</p>
  <span class="more">Read more<b>+</b></span>
</article>
<article class="promo abs" style="left:324px">
  <h3>Coaching</h3>
  <p>Lorem ipsum dolor sit amet, consectetur adipisicing elit, sed do eiusmod tempor incididunt ut labore et dolore magna aliqua. Ut enim ad minim veniam, quis nostrud exercitation ullamco laboris nisi ut aliquip ex ea commodo consequat.</p>
  <span class="more">Read more<b>+</b></span>
</article>
<article class="promo abs" style="left:522px">
  <h3>Kit</h3>
  <p>Lorem ipsum dolor sit amet, consectetur adipisicing elit, sed do eiusmod tempor incididunt ut labore et dolore magna aliqua. Ut enim ad minim veniam, quis nostrud exercitation ullamco laboris nisi ut aliquip ex ea commodo consequat.</p>
  <span class="more">Read more<b>+</b></span>
</article>

<div class="promo-icon abs" style="left:187px">
  <svg width="32" height="32" viewBox="0 0 32 32"><path d="M3 8l8-3 10 3 8-3v19l-8 3-10-3-8 3z" fill="#fff"/><path d="M11 5v19M21 8v19" stroke="#333" stroke-width="1.5"/><circle cx="24" cy="6" r="3.5" fill="#fff" stroke="#333"/></svg>
</div>
<div class="promo-icon abs" style="left:385px">
  <svg width="32" height="32" viewBox="0 0 32 32"><path d="M9 4h14v8a7 7 0 0 1-14 0z" fill="#fff"/><path d="M9 7H4c0 5 3 7 5 7M23 7h5c0 5-3 7-5 7" fill="none" stroke="#fff" stroke-width="2"/><rect x="14" y="19" width="4" height="5" fill="#fff"/><rect x="10" y="24" width="12" height="4" fill="#fff"/></svg>
</div>
<div class="promo-icon abs" style="left:582px">
  <svg width="32" height="32" viewBox="0 0 32 32"><ellipse cx="16" cy="16" rx="15" ry="9" transform="rotate(-45 16 16)" fill="#fff"/><path d="M11 21 21 11M13 15l4 4M15 13l4 4" stroke="#333" stroke-width="1.6"/></svg>
</div>

<h2 class="section-title abs" style="left:128px">How it Works</h2>
<h2 class="section-title abs" style="left:523px">Testimonials</h2>
<div class="rule abs"></div>

<ul class="tabs abs">
  <li class="active">Age Groups</li>
  <li>How the lessons work</li>
  <li>Learn about Activities</li>
  <li>Where you can buy kits</li>
</ul>

<div class="groups abs">
  <div class="group">
    <svg width="26" height="28" viewBox="0 0 26 28"><path d="M8 2 2 6l3 6 3-2v16h10V10l3 2 3-6-6-4c-1 2-3 3-5 3S9 4 8 2z" fill="#d42a2a"/></svg>
    <p><strong>Red age group details,</strong> Lorem ipsum dolor sit amet, consectetur adipisicing elit, sed do eiusmod tempor</p>
  </div>
  <div class="group">
    <svg width="26" height="28" viewBox="0 0 26 28"><path d="M8 2 2 6l3 6 3-2v16h10V10l3 2 3-6-6-4c-1 2-3 3-5 3S9 4 8 2z" fill="#3bb54a"/></svg>
    <p><strong>Green age group details,</strong> Lorem ipsum dolor sit amet, consectetur icing&nbsp; sed do eiusmod tempor</p>
  </div>
  <div class="group">
    <svg width="26" height="28" viewBox="0 0 26 28"><path d="M8 2 2 6l3 6 3-2v16h10V10l3 2 3-6-6-4c-1 2-3 3-5 3S9 4 8 2z" fill="#2f6fd6"/></svg>
    <p><strong>Blue age group details,</strong> Lorem ipsum dolor sit amet, consectetur adipisicing elit, sed do eiusmod tempor</p>
  </div>
</div>

<blockquote class="quote abs">
  <p>I've had the pleasure of working with Owen for a number of years. In that time I have seen what he's done for the kids to develop their rugby skills and to be honest I've found it inspirational. Owen is a true leader, the kids sit up and listen to him, which is no easy task.</p>
  <cite>- Delia Forsythe</cite>
</blockquote>

<footer>
  <div class="footer-shade abs"></div>
  <div class="footer abs"></div>

  <div class="fcol abs" style="left:127px">
    <h4>About Us</h4>
    <p>Lorem ipsum dolor sit amet, consectetur adipisicing elit, sed do eiusmod tempor incididunt ut labore et dolore magna aliqua. Ut enim ad minim veniam, quis nostrud exercitation ullamco laboris nisi ut aliquip ex ea commodo consequat.</p>
  </div>

  <div class="fcol abs" style="left:276px">
    <h4>Latest Blogs</h4>
    <p class="date">25 November 2013</p>
    <p class="post">Lorem ipsum dolor sit amet, consectetur adipisicing elit, sed do</p>
    <p class="date">25 November 2013</p>
    <p class="post">Lorem ipsum dolor sit amet, consectetur adipisicing elit, sed do</p>
  </div>

  <div class="fcol abs" style="left:423px">
    <h4>Get in Touch</h4>
    <p>If you have any questions don't hesitate to contact us</p>
    <div class="contact-line">
      <svg width="10" height="12" viewBox="0 0 10 12"><path d="M5 0a4 4 0 0 1 4 4c0 3-4 8-4 8S1 7 1 4a4 4 0 0 1 4-4z" fill="#d42a2a"/><circle cx="5" cy="4" r="1.5" fill="#3a3a3a"/></svg>
      <p>Address: KW7 4LP SCOTLAND. Hazelbank Old School House T. Varga</p>
    </div>
    <div class="contact-line">
      <svg width="10" height="11" viewBox="0 0 10 11"><path d="M2 0l2 3-1 1.5c.8 1.6 1.8 2.6 3.4 3.4L8 7l2 2-1.5 2C4 10.5 0 6.5 0 1.5z" fill="#d42a2a"/></svg>
      <p>Telephone: +00 44 908172645</p>
    </div>
    <div class="contact-line">
      <svg width="11" height="8" viewBox="0 0 11 8"><rect width="11" height="8" fill="#d42a2a"/><path d="M0 0l5.5 4L11 0" fill="none" stroke="#3a3a3a"/></svg>
      <p>Email: hello@trylinetots.uk</p>
    </div>
  </div>

  <div class="fcol abs" style="left:571px">
    <h4>Newsletter Subscribe</h4>
    <p>Stay up to date with latest news from our company. We promise we won't spam you.</p>
    <div class="subscribe"><span class="field">Enter your email here...</span><span class="send">Send</span></div>
  </div>

  <div class="footer-base abs"></div>
  <p class="copyright abs">copyrights 2013, All rights Reserved</p>
</footer>

</body>
</html>
```